Roofing Contractor business card redesign

I want to redesign my business card with a fresh, eye catching concept

Target Market(s)

Residential Roofing Clients, potential employees, and subcontractors.

Industry/Entity Type

Business

Colors

Designer to choose colors to be used in the design.

Requirements
Nice to have
• I just want something that's more pleasing to the eye. You can use a combination of either / or of my logos.

```html
<!DOCTYPE html>
<html lang="en">
<head>
<meta charset="utf-8">
<title>Fair Deal General Contractors – Business Card</title>
<link href="https://fonts.googleapis.com/css2?family=Arimo:wght@400;700&family=Oswald:wght@600&display=swap" rel="stylesheet">
<style>
  :root {
    --canvas: #5e5e5e;
    --brown: #3d1a14;
    --ink: #1b1b1b;
    --grey: #6a6a6a;
    --white: #ffffff;
    --yellow-deep: #f5b90f;
    --yellow: #f8cc1c;
    --yellow-light: #fbe569;
  }
  * { box-sizing: border-box; margin: 0; padding: 0; }
  html, body { width: 1200px; height: 1200px; overflow: hidden; }
  body {
    background: var(--canvas);
    font-family: "Arimo", Arial, sans-serif;
    display: flex;
    flex-direction: column;
    align-items: center;
    justify-content: center;
    gap: 40px;
  }
  .card {
    position: relative;
    width: 960px;
    height: 543px;
    overflow: hidden;
  }

  /* Front */
  .card-front { background: var(--white); color: var(--ink); }
  .brand {
    position: absolute;
    left: 36px; top: 36px;
    display: flex; align-items: center; gap: 28px;
  }
  .brand-mark {
    width: 185px; height: 185px; border-radius: 50%;
    background: radial-gradient(circle at 50% 40%, #f0a23a, #b5542a 55%, var(--brown) 75%);
  }
  .brand-name {
    font-weight: 700; color: var(--brown);
    font-size: 64px; line-height: 1; letter-spacing: -1px;
  }
  .brand-sub {
    font-weight: 700; color: var(--brown);
    font-size: 23px; margin-top: 6px;
  }
  .contact {
    position: absolute; left: 30px; top: 282px;
    display: flex; flex-direction: column; gap: 16px;
  }
  .contact-row { display: flex; align-items: flex-start; gap: 14px; }
  .contact-row svg { flex: none; width: 46px; height: 46px; fill: var(--brown); }
  .call-label { font-weight: 700; font-size: 34px; line-height: 1; }
  .call-number {
    font-family: "Oswald", "Arial Narrow", sans-serif;
    font-weight: 600; font-size: 44px; line-height: 1.05; color: var(--brown);
  }
  .contact-text { font-size: 29px; line-height: 1.05; }
  .person {
    position: absolute; right: 30px; top: 282px; text-align: right;
  }
  .person-name { font-weight: 700; font-size: 46px; line-height: 1.05; }
  .person-title { font-size: 25px; color: var(--grey); line-height: 1.3; }
  .person-phone {
    font-size: 28px; margin-top: 14px;
    display: inline-flex; align-items: center; gap: 12px;
  }
  .person-phone svg { width: 18px; height: 28px; }
  .web-band {
    position: absolute; right: 0; bottom: 0;
    width: 435px; height: 80px;
    background: var(--brown);
    border-top-left-radius: 42px;
    color: var(--white); font-weight: 700; font-size: 28px;
    display: flex; align-items: center; justify-content: flex-end;
    padding-right: 36px;
  }

  /* Back */
  .card-back {
    background: linear-gradient(160deg, var(--yellow-light) 0%, var(--yellow) 45%, var(--yellow-deep) 100%);
  }
  .back-scene {
    position: absolute; inset: 0;
    background:
      radial-gradient(ellipse at 35% 25%, rgba(255,245,170,0.55), transparent 55%),
      linear-gradient(180deg, transparent 55%, rgba(230,160,10,0.25) 100%);
  }
  .back-brand {
    position: absolute; left: 0; right: 0; top: 168px;
    display: flex; flex-direction: column; align-items: center;
  }
  .back-brand-row { display: flex; align-items: center; gap: 22px; }
  .back-brand-name {
    font-weight: 700; color: var(--brown);
    font-size: 110px; line-height: 1; letter-spacing: -2px;
  }
  .back-brand-mark {
    width: 170px; height: 170px; border-radius: 50%;
    background: radial-gradient(circle at 50% 40%, #f0a23a, #b5542a 55%, var(--brown) 75%);
  }
  .back-brand-sub {
    font-weight: 700; color: var(--brown); font-size: 36px; margin-top: 4px;
  }
</style>
</head>
<body>

<section class="card card-front">
  <div class="brand">
    <div class="brand-mark" role="img" aria-label="Illustrated badge of the contractor team"></div>
    <div>
      <div class="brand-name">Fair Deal</div>
      <div class="brand-sub">General Contractors, Inc.</div>
    </div>
  </div>

  <div class="contact">
    <div class="contact-row">
      <svg viewBox="0 0 24 24" aria-hidden="true"><path d="M12 1a11 11 0 1 0 0 22 11 11 0 0 0 0-22zm0 2a9 9 0 1 1 0 18 9 9 0 0 1 0-18z"/><path d="M8.6 6.2l1.6-.4 1.2 3-1.3 1a7 7 0 0 0 3.1 3.1l1-1.3 3 1.2-.4 1.6c-.2.6-.8 1-1.4.9A9.5 9.5 0 0 1 7.7 7.6c-.1-.6.3-1.2.9-1.4z"/></svg>
      <div>
        <div class="call-label">CALL US</div>
        <div class="call-number">(555) 214-7800</div>
      </div>
    </div>
    <div class="contact-row">
      <svg viewBox="0 0 24 24" aria-hidden="true"><path d="M12 1a7 7 0 0 0-7 7c0 5.3 7 15 7 15s7-9.7 7-15a7 7 0 0 0-7-7zm0 10a3 3 0 1 1 0-6 3 3 0 0 1 0 6z"/></svg>
      <div class="contact-text">4410 Maple Ridge Road Suite<br>118, Springfield TX 75000</div>
    </div>
    <div class="contact-row">
      <svg viewBox="0 0 24 24" aria-hidden="true" style="height:30px"><path d="M1 4h22v16H1zm2.6 2L12 12.4 20.4 6zM3 8v10h18V8l-9 6.8z"/></svg>
      <div class="contact-text">sam@fairdealtx.com</div>
    </div>
  </div>

  <div class="person">
    <div class="person-name">Sam Whitlock</div>
    <div class="person-title">Keller Certified Roof Inspector</div>
    <div class="person-title">Licensed Property Adjuster</div>
    <div class="person-phone">(555) 318-6042
      <svg viewBox="0 0 12 20" aria-hidden="true"><rect x="1" y="1" width="10" height="18" rx="1.5" fill="none" stroke="#1b1b1b" stroke-width="1.6"/></svg>
    </div>
  </div>

  <div class="web-band">www.fairdealgc.com</div>
</section>

<section class="card card-back">
  <div class="back-scene" role="img" aria-label="Faint outlines of house rooftops and windows"></div>
  <div class="back-brand">
    <div class="back-brand-row">
      <span class="back-brand-name">Fair</span>
      <div class="back-brand-mark" role="img" aria-label="Illustrated badge of the contractor team"></div>
      <span class="back-brand-name">Deal</span>
    </div>
    <div class="back-brand-sub">General Contractors, Inc.</div>
  </div>
</section>

</body>
</html>
```